Brightmoor Co Trade Show Flyer

We need a brochure design (8.5 x 11) Info in the design (refer to rough draft I drew on Paper): "#1 selling tool to aquire new franchisees has been video testimonials" - Martin L. Greaves, C.E.O Kolva Smoothie Franchise Testimonials - Let your franchisees do the selling for you. Franchisee testimonial: $10,000 / per Franchisee Includes: • 2 minute Video • 1 minute add for your franchise's location • Concept creation • Communication with franchisee • Travel to their location • All rental equipment • 1 round of corrections • Animated logo • Licensed music ******* For 25% Discount section (next to middle box), please put the "Venture Fairground Logo" Great to use on all your social media (USE logos and icons) • Website • Tubely • Proline • Friendly • Snapgram • Chirper • Phone calls • Emails • In person meetings Some of our clients: (use the logos I uploaded - in round boxes as in draft) LOGO (Brightmoor Franchise Testimonial) www.brightmoorstories.example (866) 555-0187

Target Market(s)

Franchise owners

Colors

Designer to choose colors to be used in the design.

Requirements

```html
<!DOCTYPE html>
<html lang="en">
<head>
<meta charset="utf-8">
<title>Brightmoor Franchise Testimonials Flyer</title>
<link href="https://fonts.googleapis.com/css2?family=Montserrat:wght@400;500;600;700&family=Oswald:wght@500;600&display=swap" rel="stylesheet">
<style>
  :root{
    --red:#f03a37;
    --ink:#1e1e1e;
    --charcoal:#333335;
    --page:#ffffff;
    --backdrop:#9a9a9a;
    --strip:#f4f4f4;
    --teal:#1aa38a;
  }
  *{box-sizing:border-box;margin:0;padding:0}
  html,body{width:1200px;height:1200px;overflow:hidden;background:var(--backdrop)}
  body{font-family:"Montserrat",sans-serif;color:var(--ink)}
  .flyer{position:absolute;left:159px;top:33px;width:882px;height:1134px;background:var(--page);overflow:hidden}
  .hero-photo{position:absolute;left:0;top:0;width:882px;height:328px;
    background:linear-gradient(100deg,#c9c2b6 0%,#a49a8c 28%,#5d6677 55%,#2c3850 78%,#1f2a40 100%)}
  .quote-box{position:absolute;left:40px;top:266px;width:801px;height:96px;background:var(--charcoal);
    border-radius:10px;color:#fff;text-align:center;padding-top:26px;box-shadow:0 10px 14px -8px rgba(0,0,0,.35)}
  .quote-box .mark{position:absolute;color:var(--red);font-family:"Oswald",sans-serif;font-size:44px;font-weight:600;line-height:1}
  .quote-box .open{left:26px;top:12px}
  .quote-box .close{right:20px;top:30px}
  .quote-text{font-size:19px;font-weight:500;letter-spacing:.2px}
  .quote-text strong{font-weight:700}
  .quote-by{color:var(--red);font-weight:700;font-size:18px;margin-top:10px}
  .headline{position:absolute;left:0;width:882px;top:392px;text-align:center;color:var(--red);
    font-weight:700;font-size:55px;letter-spacing:1.5px;line-height:1}
  .subhead{position:absolute;left:0;width:882px;top:451px;text-align:center;font-weight:600;font-size:23px;letter-spacing:.6px}
  .discount{position:absolute;left:31px;top:504px;width:180px;height:180px}
  .discount-text{position:absolute;left:31px;top:504px;width:180px;height:180px;color:#fff;text-align:center}
  .discount-label{position:absolute;top:41px;left:88px;font-family:"Oswald",sans-serif;font-size:13px;font-weight:500}
  .discount-value{position:absolute;top:54px;left:40px;font-weight:700;font-size:47px;line-height:1}
  .partner-badge{position:absolute;left:55px;top:101px;width:70px;height:44px;background:var(--teal)}
  .price-pill{position:absolute;left:258px;top:513px;width:455px;height:38px;background:var(--red);border-radius:4px;
    color:#fff;font-weight:700;font-size:21px;text-align:center;line-height:38px}
  .includes{position:absolute;top:570px;list-style:none;font-size:16px;line-height:25px}
  .includes li{position:relative;padding-left:28px}
  .includes li::before{content:"";position:absolute;left:2px;top:8px;width:10px;height:10px;border-radius:50%;background:var(--red)}
  .includes.left{left:232px;width:230px}
  .includes.right{left:529px;width:320px}
  .section-rule{position:absolute;left:0;width:882px;text-align:center;font-family:"Oswald",sans-serif;font-weight:500;
    color:var(--red);font-size:22px;letter-spacing:.3px;display:flex;justify-content:center;align-items:center;gap:10px}
  .section-rule::before,.section-rule::after{content:"";width:45px;height:2px;background:var(--ink)}
  .rule-uses{top:717px}
  .rule-trusted{top:838px}
  .channels{position:absolute;top:764px;left:213px;display:flex;gap:15px}
  .channel{width:43px;height:43px;border-radius:50%;background:var(--charcoal);color:#fff;display:flex;align-items:center;justify-content:center;
    font-size:8px;font-weight:700}
  .channel svg{width:22px;height:22px}
  .client-strip{position:absolute;left:45px;top:882px;width:787px;height:112px;background:var(--strip);
    display:flex;align-items:center;justify-content:space-around;padding:0 30px;box-shadow:-3px 0 4px -2px rgba(0,0,0,.25),3px 0 4px -2px rgba(0,0,0,.25)}
  .client{background:#fff;height:82px;display:flex;align-items:center;justify-content:center;gap:6px;
    font-weight:700;font-size:13px;color:var(--ink);padding:0 10px;text-align:center}
  .client .dot{width:12px;height:12px;border-radius:50%;background:var(--red);flex:none}
  .brand{position:absolute;left:40px;top:1018px;width:155px;text-align:center}
  .brand-name{font-weight:700;font-size:21px;letter-spacing:.5px}
  .brand-sub{font-size:7px;font-weight:600;letter-spacing:.4px;margin-top:2px}
  .contact{position:absolute;top:1039px;display:flex;align-items:center;gap:14px;font-size:17px;letter-spacing:.4px}
  .contact .icon{width:42px;height:42px;border-radius:50%;background:var(--charcoal);display:flex;align-items:center;justify-content:center}
  .contact .icon svg{width:22px;height:22px}
  .contact-phone{left:266px}
  .contact-web{left:526px}
  .base-band{position:absolute;left:0;bottom:0;width:882px;height:25px;background:var(--red)}
</style>
</head>
<body>
<main class="flyer">
  <div class="hero-photo" role="img" aria-label="Photo of two businessmen in suits reviewing a tablet at a desk"></div>

  <blockquote class="quote-box">
    <span class="mark open">&ldquo;</span>
    <p class="quote-text"><strong>#1</strong> selling tool to aquire new franchisees has been video testimonials</p>
    <p class="quote-by">- Martin L. Greaves, C.E.O</p>
    <span class="mark close">&rdquo;</span>
  </blockquote>

  <h1 class="headline">FRANCHISE TESTIMONIALS</h1>
  <p class="subhead">LET YOUR FRANCHISEES DO THE SELLING FOR YOU.</p>

  <svg class="discount" viewBox="-90 -90 180 180" aria-hidden="true">
    <g fill="#f03a37">
      <rect x="-66" y="-66" width="132" height="132"/>
      <rect x="-66" y="-66" width="132" height="132" transform="rotate(11.25)"/>
      <rect x="-66" y="-66" width="132" height="132" transform="rotate(22.5)"/>
      <rect x="-66" y="-66" width="132" height="132" transform="rotate(33.75)"/>
      <rect x="-66" y="-66" width="132" height="132" transform="rotate(45)"/>
      <rect x="-66" y="-66" width="132" height="132" transform="rotate(56.25)"/>
      <rect x="-66" y="-66" width="132" height="132" transform="rotate(67.5)"/>
      <rect x="-66" y="-66" width="132" height="132" transform="rotate(78.75)"/>
    </g>
  </svg>
  <div class="discount-text">
    <span class="discount-label">DISCOUNT</span>
    <span class="discount-value">25%</span>
    <span class="partner-badge" role="img" aria-label="Venture Fairground badge"></span>
  </div>

  <div class="price-pill">$10,000 / per Franchisee Includes:</div>
  <ul class="includes left">
    <li>2 minute Video</li>
    <li>1 minute add for your franchise's location</li>
    <li>Concept creation</li>
  </ul>
  <ul class="includes right">
    <li>Communication with franchisee</li>
    <li>Travel to their location</li>
    <li>All rental equipment</li>
    <li>1 round of corrections</li>
  </ul>

  <h2 class="section-rule rule-uses">USE YOUR TESTIMONIALS EVERYWHERE</h2>
  <div class="channels">
    <span class="channel">Friendly</span>
    <span class="channel">Tubely</span>
    <span class="channel">Snapgram</span>
    <span class="channel" aria-label="Website"><svg viewBox="0 0 24 24" fill="none" stroke="#fff" stroke-width="1.8"><circle cx="12" cy="12" r="9"/><ellipse cx="12" cy="12" rx="4" ry="9"/><path d="M3 12h18M5 7h14M5 17h14"/></svg></span>
    <span class="channel" aria-label="Phone"><svg viewBox="0 0 24 24" fill="#fff"><path d="M7 3l3 4-2 2c1 2.5 3.5 5 6 6l2-2 4 3-2 4C10 19 5 14 4 6z"/></svg></span>
    <span class="channel" aria-label="Email"><svg viewBox="0 0 24 24" fill="none" stroke="#fff" stroke-width="1.8"><rect x="3" y="6" width="18" height="12"/><path d="M3 6l9 7 9-7"/></svg></span>
    <span class="channel">Proline</span>
    <span class="channel">Chirper</span>
  </div>

  <h2 class="section-rule rule-trusted">TRUSTED BY</h2>
  <div class="client-strip">
    <div class="client" style="width:100px;border-radius:50%"><span class="dot"></span>Scoopwell</div>
    <div class="client" style="width:110px"><span class="dot"></span>Dayround Mart</div>
    <div class="client" style="width:115px"><span class="dot"></span>Kolva Smoothie</div>
    <div class="client" style="width:82px">Tidecrest Cleaning</div>
    <div class="client" style="width:152px;height:74px"><span class="dot"></span>Gearline Car Care</div>
  </div>

  <div class="brand">
    <div class="brand-name">BRIGHTMOOR</div>
    <div class="brand-sub">FRANCHISE TESTIMONIAL</div>
  </div>
  <div class="contact contact-phone">
    <span class="icon"><svg viewBox="0 0 24 24" fill="#fff"><path d="M7 3l3 4-2 2c1 2.5 3.5 5 6 6l2-2 4 3-2 4C10 19 5 14 4 6z"/></svg></span>
    <span>(866) 555-0187</span>
  </div>
  <div class="contact contact-web">
    <span class="icon"><svg viewBox="0 0 24 24" fill="none" stroke="#fff" stroke-width="1.8"><circle cx="12" cy="12" r="9"/><ellipse cx="12" cy="12" rx="4" ry="9"/><path d="M3 12h18M5 7h14M5 17h14"/></svg></span>
    <span>www.brightmoorstories.example</span>
  </div>

  <div class="base-band"></div>
</main>
</body>
</html>
```